Design some Business Cards for my concierge service company

Hi Freelancers

I would need you to design some business cards for my company, the name of the company is (VelvetRopeHub).

Please find the vector logo attached.

Here are the information that should appear on the business card:

Name: Marlo Venturi
Job Tittle: CO-Founder
Email: info@velvetropehub.com
Phone: +971 50 386 2071
Website: www.velvetropehub.ae

Facebook/Twiter/instagram: VelvetRopeHubDubai

the main color are White, Black and gold. Keep in mind that I want the logo with gold foiling

For your information, the company will be offering concierge service for clubs in Dubai. So the business card should look very classy, proffesional and rich

Thanks for your entries

```html
<!DOCTYPE html>
<html lang="en">
<head>
<meta charset="utf-8">
<title>VelvetRopeHub Business Cards</title>
<link rel="stylesheet" href="https://fonts.googleapis.com/css2?family=Open+Sans:wght@300;400;600&display=swap">
<style>
  :root {
    --bg: #e8e3db;
    --card-dark: #1f0f0c;
    --card-dark-edge: #140907;
    --gold: #c9a24a;
    --gold-line: #d4b05a;
    --paper: #ffffff;
    --ink: #1a1a1a;
    --shadow: rgba(40, 25, 15, 0.35);
  }
  * { box-sizing: border-box; margin: 0; padding: 0; }
  html, body {
    width: 1200px;
    height: 843px;
    overflow: hidden;
    background: var(--bg);
    font-family: "Open Sans", sans-serif;
  }
  .canvas {
    position: relative;
    width: 1200px;
    height: 843px;
  }
  .card {
    position: absolute;
    top: 278px;
    width: 500px;
    height: 286px;
    border-radius: 4px;
    box-shadow: 0 14px 30px var(--shadow);
    overflow: hidden;
  }
  .card--front {
    left: 70px;
    background: linear-gradient(160deg, #2a1612 0%, var(--card-dark) 55%, var(--card-dark-edge) 100%);
    display: flex;
    align-items: center;
    justify-content: center;
    gap: 14px;
  }
  .brand-dot {
    width: 16px;
    height: 16px;
    border-radius: 50%;
    background: var(--gold);
  }
  .brand-name {
    color: var(--gold);
    font-weight: 600;
    font-size: 34px;
    letter-spacing: 1px;
  }
  .card--back {
    left: 630px;
    background: var(--card-dark);
  }
  .back-panel {
    position: absolute;
    left: 10px;
    right: 10px;
    top: 26px;
    bottom: 44px;
    background: var(--paper);
    border: 2px solid var(--gold-line);
    color: var(--ink);
  }
  .holder {
    position: absolute;
    top: 22px;
    left: 0;
    right: 0;
    text-align: center;
    padding-left: 120px;
  }
  .holder-name {
    font-size: 21px;
    font-weight: 400;
    line-height: 1.2;
  }
  .holder-title {
    font-size: 16px;
    font-weight: 300;
  }
  .contacts {
    position: absolute;
    top: 104px;
    left: 150px;
    list-style: none;
    font-size: 17px;
    line-height: 1.45;
  }
  .contacts li {
    display: flex;
    align-items: center;
    gap: 8px;
  }
  .contacts svg { width: 17px; height: 17px; flex: none; }
  .website {
    position: absolute;
    left: 170px;
    bottom: 12px;
    font-size: 17px;
  }
</style>
</head>
<body>
<main class="canvas">
  <section class="card card--front" aria-label="Card front">
    <span class="brand-dot"></span>
    <span class="brand-name">VelvetRopeHub</span>
  </section>

  <section class="card card--back" aria-label="Card back">
    <div class="back-panel">
      <div class="holder">
        <p class="holder-name">Marlo Venturi</p>
        <p class="holder-title">CO-Founder</p>
      </div>
      <ul class="contacts">
        <li>
          <svg viewBox="0 0 20 20" aria-hidden="true"><circle cx="10" cy="10" r="8.5" fill="none" stroke="#1a1a1a" stroke-width="1.5"/><rect x="5" y="6.5" width="10" height="7" fill="none" stroke="#1a1a1a" stroke-width="1.3"/><path d="M5 6.5l5 4 5-4" fill="none" stroke="#1a1a1a" stroke-width="1.3"/></svg>
          info@velvetropehub.com
        </li>
        <li>
          <svg viewBox="0 0 20 20" aria-hidden="true"><path d="M5 2.5l3 3-1.6 2.2c1 2.1 2.7 3.8 4.9 4.9L13.5 11l3 3-2 3c-6.5-.6-11.4-5.5-12-12z" fill="#1a1a1a"/></svg>
          +971 50 386 2071
        </li>
      </ul>
      <p class="website">www.velvetropehub.ae</p>
    </div>
  </section>
</main>
</body>
</html>
```